Design a cool print brochure for an NGO / Give your work a global impact!!

Hi,
I provide a full design brief (below, please scroll) and a mood board (attached) to help you visualize inside my head.. ;-)
I am also available to help and have worked many years in advertising; we will understand each other.
Objective:
To design an A4 folded in two presentation brochure for a non-profit consulting agency called Mer-ova.
Mer-ova works in sustainability and international development = working with NGO’s, governments and private sector on global issues such as global warming, education for all etc.
Strategy:
This document is a first step in developing a communication strategy. It will be distributed during a major international event called the Brenvik Outreach Forum.
Objective:
The double objective of the brochure is:
a) to inform the recipient of what Mer-ova is, in the shortest time possible.
b) to showcase relevant projects to demonstrate Mer-ova experience and expertise.
Target:
Main target:
Existing Mer-ova contacts, such as members of development organizations, NGOs, private sector foundations (CSR), regional networks and other development actors.
NB: the main target already has a certain awareness of Mer-ova: we will try to minimize text to maximize visual impact and readability.
Secondary target:
Mer-ova will also distribute the brochure to new prospects of interest during the Brenvik Forum.
Timing:
We will need to finalize the design and have the files by June 1st to allow time for print before the event.
Content:
The document should be concise, highly readable (no clutter) and include:
1. text (that we will provide)
and
2. visual elements such as images, shapes and info-graphics (that is you).
NB: Mer-ova does not have its own image bank; photos will be provided by you.
Format:
A4 folded in half - 4pp A5 - PORTRAIT FORMAT) with an impactful visual in the front, logo, title and headline (please see examples in the mood board attached).
Design elements:
Mer-ova does not have yet a visual identity (please see: http://mer-ova.org) so there is room for creativity and no graphic chart to follow.
The sector of consulting in international development is rather conservative but our intention is to be disruptive and create a “Wow” effect. We count on you for that!
Therefore, the design should be “structured”, “organized”, “uncluttered” but also “modern”, “impactful”, “highly visual” (think infographic or mind map to describe our services and projects).
Please, take the time to see the attached presentation: I give you guidelines and examples of what we want and what we like.
We are looking forward to seeing your work and I am available for comments, questions and support.
Thank you.
RM
Target Market(s)
The full brief is in the project description: please, scroll through it.
The target market is : our existing clients base, working in sustainable development (read: NGO and Concord Assembly people)
Industry/Entity Type
Ngo
Requirements
Must have
- - Design and color elements: please, no black and white. Our company website is in black and white and without graphics; we want the brochure to break away from that and start creating our brand identity; so please, show us colors and desing elements (shapes, backgrounds, etc).
- You have a chance to showcase your talent in terms of visual identity: what lines, forms, layout and colors can you come up with and apply throughout the brochure and serve as the visual identity of Mer-ova?
- The structure of the document should be:
- - Front cover: design elements + impacful photo (see mood board example attached) +our logo + this headline: "Collective action for sustainable development and impact"
- - Inside front: a graphic representation of "Our Services": such as core activity in the center circle and satellite circles for the services we offer.
- - Inside back:
- 1. Icons and text boxes for "Our projects"
- 2. A world map of the countries where we have worked. Full list of countries is here:
- http://mer-ova.org/experience-1
- - Back cover: our contact + logos of partners.
- Our partners are listed here:
- Please use their original logos (ie, in color).
- The design we will select will serve as a basis for a graphic chart...so more work to come...word to the wise ;)
- Please check out our website mer-ova.org to see what we do etc.
Nice to have
- Icons to reflect our services: what icons can you come up with to describe "training services", "building networks" or "program management"?
- I give examples in the mood board.
Should not have
- We are open to creativity and want to generate a "Wow" effect.
- Just note that the sector is rather conservative so flashy colors and cartoon like characters should be avoided. Think "earth, global change, Concord Assembly, climate" without going too green (it's overdone). ;-)
- Make us stand out in the NGO world
- Now you.

```html
<!DOCTYPE html>
<html lang="en">
<head>
<meta charset="utf-8">
<title>Mer-ova — brochure spreads</title>
<link href="https://fonts.googleapis.com/css2?family=Oswald:wght@300;400;500;600&display=swap" rel="stylesheet">
<style>
:root{
  --page-bg:#ececec;
  --teal:#22a893;
  --teal-light:#2bb39f;
  --teal-dark:#1e9886;
  --lime:#a8c93a;
  --orange:#ee7226;
  --salmon:#f2a36b;
  --olive:#a9a87a;
  --white:#ffffff;
  --ink:#2b2b2b;
  --un-blue:#4a8fd0;
}
*{margin:0;padding:0;box-sizing:border-box}
html,body{width:1200px;height:1200px;overflow:hidden;background:var(--page-bg)}
body{position:relative;font-family:"Oswald",sans-serif}
.spread{position:absolute;left:256px;width:747px;height:528px;overflow:hidden;box-shadow:0 2px 6px rgba(0,0,0,.18)}
.spread--outside{top:65px;background:var(--white)}
.spread--inside{top:609px;background:var(--teal)}
.abs{position:absolute}
svg.overlay{position:absolute;left:0;top:0;width:747px;height:528px;pointer-events:none}

/* back cover */
.back-page{position:absolute;left:0;top:0;width:372px;height:528px}
.section-label{position:absolute;color:var(--orange);font-weight:500;font-size:15px;letter-spacing:.2px;text-transform:uppercase;white-space:nowrap}
.partner--concord{position:absolute;display:flex;flex-direction:column;align-items:center;gap:3px;color:var(--un-blue);font-size:5.5px;font-weight:500;text-transform:uppercase;white-space:nowrap}
.partner--concord .seal{width:36px;height:36px;border-radius:50%;background:var(--un-blue)}
.badge{position:absolute;border-radius:2px}
.contact-text{position:absolute;left:172px;top:459px;width:160px;text-align:right;font-size:4.3px;line-height:5.3px;color:var(--ink);text-transform:uppercase;font-weight:400}
.contact-lines{position:absolute;left:232px;top:486px;width:100px;text-align:right;font-size:4.4px;line-height:5.4px;font-weight:600;color:var(--ink)}
.footer-band{position:absolute;left:56px;top:503px;width:277px;height:40px;background:var(--orange);border-radius:22px 22px 0 0}

/* front cover */
.cover{position:absolute;left:372px;top:0;width:375px;height:528px;background:radial-gradient(ellipse at 60% 45%,var(--teal-light),var(--teal) 60%,var(--teal-dark))}
.cover-photo-bulb{position:absolute;left:148px;top:144px;width:78px;height:160px;border-radius:40px 40px 20px 20px;background:radial-gradient(circle at 50% 30%,#f6fffc,#bfe9df 70%,rgba(191,233,223,0))}
.cover-photo-balls{position:absolute;left:40px;top:370px;width:300px;height:120px;background:radial-gradient(circle at 25% 30%,rgba(232,111,40,.9) 0 28px,transparent 30px),radial-gradient(circle at 65% 55%,rgba(232,111,40,.9) 0 34px,transparent 36px),radial-gradient(circle at 87% 55%,rgba(232,111,40,.9) 0 36px,transparent 38px)}
.brand{position:absolute;left:237px;top:152px;color:var(--white);font-size:38px;font-weight:400;letter-spacing:-.5px;line-height:1}
.tagline{position:absolute;left:231px;top:228px;width:144px;height:34px;background:rgba(255,255,255,.3)}
.tagline-text{position:absolute;right:24px;top:2px;text-align:right;font-size:9.6px;line-height:10.3px;text-transform:uppercase;font-weight:400;white-space:nowrap}
.tagline .o{color:var(--orange)}
.tagline .l{color:var(--lime)}

/* inside */
.lime-top{position:absolute;left:0;top:0;width:332px;height:22px;background:var(--lime);border-radius:0 0 14px 0}
.lime-spine{position:absolute;left:372px;top:0;width:21px;height:528px;background:var(--lime);border-radius:14px 0 0 14px}
.heading{position:absolute;color:var(--lime);font-size:31px;font-weight:500;line-height:1;letter-spacing:-.3px;text-transform:uppercase;white-space:nowrap}
.intro{position:absolute;left:54px;top:82px;width:280px;text-align:center;color:var(--lime);font-size:4.4px;line-height:5.4px;text-transform:uppercase;font-weight:300}
.core{position:absolute;left:42px;top:145px;width:129px;height:129px;border:1px solid var(--orange);border-radius:50%;display:flex;flex-direction:column;align-items:center;justify-content:center;text-transform:uppercase;line-height:1.12;text-align:center;white-space:nowrap}
.core .sal{color:var(--salmon)}
.core .org{color:var(--orange)}
.core .lg{font-size:17px;font-weight:500}
.core .md{font-size:13px;font-weight:500}
.core .sm{font-size:10px}
.service{position:absolute;text-align:center;color:var(--orange);font-size:8.4px;line-height:12.5px;text-transform:uppercase;font-weight:400;white-space:nowrap}
.service u{text-decoration:none;border-bottom:3px solid var(--lime);padding-bottom:1px}
.region{position:absolute;color:var(--white);font-size:19px;font-weight:500;line-height:1;text-transform:uppercase;white-space:nowrap}
.countries{position:absolute;color:var(--white);font-size:4.2px;line-height:5.2px;text-transform:uppercase;text-align:right;font-weight:300}
.map{position:absolute;left:478px;top:418px;width:234px;height:82px;background:linear-gradient(120deg,#d95bb0 0%,#d95bb0 45%,#f3c9a8 62%,#f3c9a8 100%);border-radius:30px 16px 26px 40px;opacity:.9}
</style>
</head>
<body>

<section class="spread spread--outside">
  <div class="back-page">
    <svg class="abs" style="left:0;top:0" width="372" height="528" viewBox="0 0 372 528" aria-hidden="true">
      <line x1="56" y1="281" x2="253" y2="281" stroke="#a8c93a" stroke-width="1.3" stroke-dasharray="3 3"/>
      <line x1="56" y1="448" x2="267" y2="448" stroke="#a8c93a" stroke-width="1.3" stroke-dasharray="3 3"/>
    </svg>

    <div class="section-label" style="left:260px;top:270px">Our partners</div>
    <div class="partner--concord" style="left:52px;top:298px"><span class="seal"></span>Concord Assembly</div>
    <div class="badge" style="left:113px;top:303px;width:45px;height:31px;background:#2b3e93"></div>
    <div class="badge" style="left:175px;top:302px;width:44px;height:32px;background:#c5cfc7;border-radius:50%"></div>
    <div class="badge" style="left:238px;top:302px;width:76px;height:32px;background:#3b8cc9"></div>
    <div class="badge" style="left:56px;top:354px;width:82px;height:24px;background:#8a8a8a"></div>
    <div class="badge" style="left:150px;top:359px;width:76px;height:12px;background:#2a4d8f"></div>
    <div class="badge" style="left:244px;top:349px;width:90px;height:30px;background:#5bb34a;border-radius:50%"></div>
    <div class="badge" style="left:56px;top:393px;width:68px;height:22px;background:#2e5a9a"></div>
    <div class="badge" style="left:159px;top:391px;width:72px;height:26px;background:#9b2f3a"></div>
    <div class="badge" style="left:248px;top:394px;width:84px;height:20px;background:#c1272d"></div>

    <div class="section-label" style="left:273px;top:437px">Contact us</div>
    <p class="contact-text">We are based in different cities in Europe. You can contact any of us directly in About us. Alternatively, for general inquiries, you can use the number and/or email below.</p>
    <p class="contact-lines">T: +34 600 417 229<br>E: INFO@MER-OVA.ORG</p>
    <div class="footer-band"></div>
  </div>

  <div class="cover">
    <div class="abs" role="img" aria-label="Photograph: glowing white energy-saving light bulb with orange glass bulbs lying on a teal surface" style="inset:0">
      <div class="cover-photo-bulb"></div>
      <div class="cover-photo-balls"></div>
    </div>
    <svg class="abs" style="left:0;top:0" width="375" height="528" viewBox="0 0 375 528" aria-hidden="true">
      <polyline points="196,146 354,146 354,306 186,306" fill="none" stroke="#fff" stroke-width="1" stroke-dasharray="3 2"/>
    </svg>
    <div class="brand">mer-ova</div>
    <div class="tagline">
      <p class="tagline-text"><span class="o">Collective action</span><br><span class="o">for </span><span class="l">sustainable</span><br><span class="l">development </span><span class="o">and </span><span class="l">impact</span></p>
    </div>
  </div>
</section>

<section class="spread spread--inside">
  <div class="lime-top"></div>
  <div class="lime-spine"></div>

  <h2 class="heading" style="left:120px;top:43px">Our services</h2>
  <p class="intro">Mer-ova specializes in the analysis of multi-actor cooperation and the facilitation of processes of change. We believe in the need to improve both the understanding and use of collaborative action. For that, we support value-oriented organisations to integrate a better cooperation logic in their daily practice, whether as part of their internal management or in the context of their relations with other stakeholders. We see our clients as our most important partners. Through them we learn and improve our knowledge about the challenges of collaborative action. We avoid prefabricated solutions and engage with them to find answers that fit each assignment.</p>

  <svg class="overlay" viewBox="0 0 747 528" aria-hidden="true">
    <g fill="none" stroke="#a8c93a" stroke-width=".8" stroke-dasharray="3 2">
      <polyline points="148,155 185,130 236,167"/>
      <polyline points="150,262 160,273 245,269"/>
      <polyline points="122,277 128,297 128,325"/>
      <polyline points="135,275 170,320 265,357"/>
      <polyline points="145,273 210,400 212,420"/>
      <polyline points="55,260 15,340 45,440"/>
    </g>
    <path d="M157,157 A70,70 0 0 1 176,258" fill="none" stroke="#a9a87a" stroke-width="8"/>
    <path d="M93,141 A75,75 0 0 0 63,250" fill="none" stroke="#a9a87a" stroke-width="2.5"/>
    <g fill="none" stroke="#a8c93a" stroke-width="1.4">
      <circle cx="291" cy="163" r="9"/><line x1="299" y1="167" x2="328" y2="175"/>
      <circle cx="328" cy="264" r="16"/><line x1="312" y1="264" x2="344" y2="264"/><line x1="328" y1="248" x2="328" y2="280"/>
      <circle cx="65" cy="322" r="3"/><circle cx="82" cy="322" r="3"/><circle cx="78" cy="301" r="3"/><polyline points="68,320 78,304 92,292"/><polyline points="86,290 92,292 90,298"/>
      <rect x="279" y="325" width="14" height="22"/><rect x="295" y="337" width="21" height="28"/>
      <polyline points="243,416 243,404 255,396 274,396"/><polyline points="277,404 277,416 265,424 248,424"/>
      <circle cx="251" cy="425" r="7"/><circle cx="261" cy="425" r="7"/><circle cx="271" cy="425" r="7"/><path d="M238,455 v-14 h40 v14"/>
      <path d="M146,418 a22,22 0 1 1 0,30"/><polyline points="142,444 146,450 152,446"/>
    </g>
    <g fill="none" stroke="#fff" stroke-width=".8" stroke-dasharray="3 2">
      <polyline points="459,376 459,365 532,365 532,418"/>
      <polyline points="478,460 482,466 482,507 592,507 592,500"/>
      <polyline points="606,418 606,398 608,340 616,340"/>
      <polyline points="704,340 727,340 727,507 633,507 633,500"/>
    </g>
  </svg>

  <div class="core">
    <span class="sal lg">Our work</span>
    <span class="sm"><span class="sal">encompasses </span><span class="org">specific</span></span>
    <span><span class="org md">Projects </span><span class="sal sm">and/or</span></span>
    <span><span class="sal sm">organisation </span><span class="org sm" style="font-weight:500">as a</span></span>
    <span class="org lg">whole.</span>
  </div>

  <p class="service" style="left:236px;top:177px">Research and analysis of<br><u>Cooperation schemes</u></p>
  <p class="service" style="left:239px;top:269px">Facilitation of<br><u>Processes of change</u></p>
  <p class="service" style="left:53px;top:331px">Training to improve<br><u>Networked action</u></p>
  <p class="service" style="left:237px;top:354px">Evaluation of<br>multi-actor projects<br><u>and programs</u></p>
  <p class="service" style="left:30px;top:430px">Methodologies for<br>organizational change and<br><u>consensus building</u></p>
  <p class="service" style="left:209px;top:457px">Coalition building to<br><u>achieve collective goals</u></p>

  <h2 class="heading" style="left:399px;top:43px">Our projects</h2>
  <h2 class="heading" style="left:401px;top:332px">Our presence</h2>

  <div class="map" role="img" aria-label="World map highlighting countries of activity in pink"></div>

  <div class="region" style="left:402px;top:381px">America</div>
  <p class="countries" style="left:402px;top:403px;width:60px">US, Canada, Guatemala, El Salvador, Panama, Costa Rica, Honduras, Colombia, Peru, Bolivia, Brazil, Argentina, Uruguay and Paraguay</p>
  <div class="region" style="left:402px;top:450px">Africa</div>
  <p class="countries" style="left:402px;top:473px;width:46px">South Africa, Mozambique, Ethiopia, Kenya, Uganda, Benin, Senegal, Zimbabwe, Ghana, Tunisia, Egypt and Libya.</p>
  <div class="region" style="left:617px;top:333px">Europe</div>
  <p class="countries" style="left:618px;top:356px;width:54px">EU 28, Norway, Switzerland, Turkey, Montenegro, Ukraine, Serbia, Moldova, Armenia, Georgia and Belarus.</p>
  <div class="region" style="left:686px;top:333px">Asia</div>
  <p class="countries" style="left:682px;top:356px;width:28px">China, Vietnam, Thailand, Indonesia, Malaysia, Singapore, Bangladesh, Kyrgyzstan, Kazakhstan and Myanmar.</p>
</section>

</body>
</html>
```